business card for LWR pty ltd

We require a business card that stands out . I have included our company flyer and would like the services listed to be put on the card so when we Give out the cards to customers they have an idea of services we provide. need the winning design to be in editable photo shop format, editable iMac pages format or editable windows publisher format, so that I can enter in names, email addresses, phone numbers etc myself. I have included a pdf documents of info / items needed on the card to use as reference please.
Updates

need more submissions

Need extra days to review

Sick

Target Market(s)

new customers

Contact Information for Business Card

details are on attached business card requirements file

Requirements
Must have
• I have attached a list of must haves

```html
<!DOCTYPE html>
<html lang="en">
<head>
<meta charset="utf-8">
<title>LWR pty ltd – Business Card</title>
<link rel="stylesheet" href="https://fonts.googleapis.com/css2?family=Montserrat:wght@500;600;700;800&family=Michroma&display=swap">
<style>
  :root {
    --page-bg: #e2e2e2;
    --card-dark: #141414;
    --card-mid: #2e2e2e;
    --silver: #d4d4d4;
    --silver-dim: #a9a9a9;
    --rule: #6e6e6e;
    --earth: #b8743e;
    --earth-dark: #6d4222;
  }
  * { box-sizing: border-box; margin: 0; padding: 0; }
  html, body { width: 1200px; height: 1200px; overflow: hidden; }
  body { background: var(--page-bg); position: relative; font-family: "Montserrat", sans-serif; }

  .card {
    position: absolute; top: 299px; width: 362px; height: 602px; overflow: hidden;
    color: var(--silver);
  }
  .card--front { left: 205px; background: linear-gradient(180deg, var(--card-mid) 36%, #262626 70%, var(--card-dark) 100%); }
  .card--back { left: 640px; background: radial-gradient(ellipse at 50% 40%, #1e1e1e 0%, #0d0d0d 100%); }

  .hero {
    position: absolute; left: 0; top: 0; width: 100%; height: 216px;
    background: linear-gradient(180deg, #0b0b0b 0%, #222 45%, #2a2a2a 65%, var(--earth-dark) 82%, var(--earth) 100%);
  }

  .brand-name {
    position: absolute; left: 0; top: 36px; width: 100%; text-align: center;
    font-family: "Montserrat", sans-serif; font-weight: 800; font-size: 84px;
    letter-spacing: 2px; color: var(--silver); line-height: 1;
  }

  .identity {
    position: absolute; left: 52px; width: 257px; top: 244px; height: 51px;
    border-top: 1px solid var(--rule); border-bottom: 1px solid var(--rule);
    text-align: center;
  }
  .identity__name {
    font-weight: 700; font-size: 26px; letter-spacing: 1.5px; line-height: 26px;
    margin-top: 4px; color: #dcdcdc;
  }
  .identity__role {
    font-family: "Michroma", sans-serif; font-size: 11px; letter-spacing: 2px;
    line-height: 12px; margin-top: 2px; color: var(--silver-dim);
  }

  .address {
    position: absolute; left: 0; width: 100%; top: 421px; text-align: center;
    font-family: "Michroma", sans-serif; font-size: 12px; letter-spacing: 1.6px; line-height: 18px; color: var(--silver-dim);
  }

  .contact-icons {
    position: absolute; left: 0; width: 100%; top: 487px;
    display: flex; justify-content: center; align-items: center; gap: 6px;
  }
  .contact-icons .divider { width: 1px; height: 16px; background: var(--rule); }

  .contact {
    position: absolute; left: 0; width: 100%; top: 512px; text-align: center;
    font-family: "Michroma", sans-serif; color: var(--silver-dim);
  }
  .contact__phone { font-size: 13px; letter-spacing: 2px; line-height: 19px; }
  .contact__line { font-size: 10.5px; letter-spacing: 1px; line-height: 18px; }

  .services-title {
    position: absolute; left: 0; width: 100%; top: 161px; text-align: center;
    font-family: "Michroma", sans-serif; font-size: 16px; letter-spacing: 3px; color: #9d9d9d;
  }
  .services {
    position: absolute; left: 0; width: 100%; top: 197px; list-style: none; text-align: center;
  }
  .services li {
    font-weight: 500; font-size: 14.2px; letter-spacing: -0.4px; line-height: 16px; color: #e4e4e4;
    padding: 0 0 15px; position: relative;
  }
  .services li + li::before {
    content: ""; position: absolute; left: 50%; top: -8px; width: 70px; height: 1px; margin-left: -35px;
    background: linear-gradient(90deg, transparent, #8a8a8a, transparent);
  }
</style>
</head>
<body>

  <section class="card card--front">
    <div class="hero" role="img" aria-label="Road train tipper trucks on red outback dirt in front of a dark honeycomb metal backdrop"></div>
    <div class="brand-name">LWR</div>

    <div class="identity">
      <p class="identity__name">DANIEL ROURKE</p>
      <p class="identity__role">DIRECTOR</p>
    </div>

    <p class="address">LOT 444 EXAMPLE<br>ADDRESS AUSTRALIA</p>

    <div class="contact-icons">
      <svg width="14" height="14" viewBox="0 0 24 24" aria-hidden="true"><path d="M6.6 10.8a15 15 0 0 0 6.6 6.6l2.2-2.2a1 1 0 0 1 1-.25 11.4 11.4 0 0 0 3.6.57 1 1 0 0 1 1 1V20a1 1 0 0 1-1 1A17 17 0 0 1 3 4a1 1 0 0 1 1-1h3.5a1 1 0 0 1 1 1c0 1.25.2 2.450.57 3.57a1 1 0 0 1-.25 1z" fill="#8c8c8c"/></svg>
      <span class="divider"></span>
      <svg width="14" height="14" viewBox="0 0 24 24" aria-hidden="true"><rect x="2" y="5" width="20" height="14" rx="1" fill="none" stroke="#8c8c8c" stroke-width="2"/><path d="M2 6l10 7 10-7" fill="none" stroke="#8c8c8c" stroke-width="2"/></svg>
      <span class="divider"></span>
      <svg width="14" height="14" viewBox="0 0 24 24" aria-hidden="true"><circle cx="12" cy="12" r="9" fill="none" stroke="#8c8c8c" stroke-width="2"/><path d="M3 12h18M12 3c3 3 3 15 0 18M12 3c-3 3-3 15 0 18" fill="none" stroke="#8c8c8c" stroke-width="1.6"/></svg>
    </div>

    <div class="contact">
      <p class="contact__phone">000 444 000</p>
      <p class="contact__line">EMAIL@LWRSERVICES.COM.AU</p>
      <p class="contact__line">WWW.WEBSITEADDRESS.COM</p>
    </div>
  </section>

  <section class="card card--back">
    <div class="brand-name">LWR</div>
    <h2 class="services-title">OUR SERVICES</h2>
    <ul class="services">
      <li>Over size loads/ Hot Shot Loads</li>
      <li>Heavy Vehicle Recovery<br>Services</li>
      <li>Portable Water Deliveries</li>
      <li>Road Building / Maintenance</li>
      <li>Earthworks</li>
      <li>Sand &amp; Metal Supply &amp; Cartage</li>
      <li>Road Train Tippers</li>
      <li>Road Train Tankers</li>
      <li>Road Train Flat Tops</li>
      <li>Drop Deck Trailers</li>
      <li>Mine Site Accredited Equipment<br>&amp; Operators</li>
    </ul>
  </section>

</body>
</html>
```